Web site for small printshop

I am looking for a website for small printshop in Iceland, mainly serving university students and artist.

We print posters, flyers, business cards and more.

In addition to our current website, I would like to include design tool, (fx. www.quarvelink.com, www.tandorizo.com or something similar) jobs upload, shopping chart.
Updates

Great work, I am really amazed of the quality of work i am seeing here.

Really way beyond my expectation

GOOD JOB - all of you ! 

Hi all.

The designs submitted have been great, way better than expected.
I really did not expect this level of quality.

Some have been asking me for feedback on their designs, and I will try 
to send some feedback here, without spoiling your creativity.

Likes:
- when the colors of my logo is used in menus, buttons etc.
- simple, not to crowded look.

Dislikes.
- Dark and heavy design
- Lot of text and buttons (crowded look)

Extra info.
- top line (before menus) will contain: Tel - email - language
- menu line will have 5 categories: Home - service - submission of works - FAQ - about us
- 3 large buttons:  Job submit - Job design - ask for offer

LOVE YOUR WORK - great designs so far :)

Target Market(s)

University Students, Artists. Age group 20-30

Industry/Entity Type

University

Requirements
Must have
• The website must be easy to use, clean looking.

```html
<!DOCTYPE html>
<html lang="en">
<head>
<meta charset="utf-8">
<title>Mosavik Studio — Printing for students and artists</title>
<link rel="stylesheet" href="https://fonts.googleapis.com/css2?family=PT+Sans:wght@400;700&family=Arimo:wght@400;700&family=Kaushan+Script&display=swap">
<style>
:root{
  --ink:#1f1d1e;
  --nav:#252223;
  --text:#333;
  --muted:#9a9a9a;
  --line:#dcdcdc;
  --panel:#e6e6e6;
  --green:#1f7a3a;
  --red:#e2362a;
  --yellow:#f3d21c;
  --white:#fff;
  --head:"PT Sans",sans-serif;
  --body:"Arimo",sans-serif;
}
*{box-sizing:border-box;margin:0;padding:0}
html,body{width:840px;height:1200px;overflow:hidden}
body{position:relative;background:var(--white);font-family:var(--body);color:var(--text)}
.page-bg{position:absolute;left:0;top:0;width:840px;height:373px;
  background:radial-gradient(circle,#d6d6d6 0.8px,transparent 1px) 0 0/9px 9px,linear-gradient(#f4f4f4,#e4e4e4)}
.abs{position:absolute}

/* top line */
.lang{left:625px;top:10px;font-size:10px;color:#555;display:flex;align-items:center;gap:5px}
.lang svg{display:block}
.brand{left:73px;top:36px}
.brand-name{font-family:var(--head);font-weight:700;font-size:27px;color:var(--ink);letter-spacing:.3px}
.contact{left:481px;top:47px;font-family:var(--head);font-size:11.5px;line-height:14px;color:var(--ink)}
.contact span{display:inline-block;width:38px}
.cart{left:666px;top:48px;width:99px;height:26px;background:#f6f6f6;border:1px solid #d8d8d8;border-radius:4px;display:flex;align-items:center;gap:5px;padding-left:2px}
.cart-icon{width:24px;height:22px;background:var(--ink);border-radius:3px;display:flex;align-items:center;justify-content:center}
.cart b{display:block;font-size:7px;color:var(--ink)}
.cart small{display:block;font-size:6px;color:#777}

/* nav */
.nav{left:73px;top:95px;width:694px;height:45px;background:var(--nav);border-radius:8px 8px 0 0;display:flex;align-items:center}
.nav a{color:var(--white);text-decoration:none;font-size:9.5px;text-transform:uppercase;height:45px;line-height:45px;padding:0 23px;border-right:1px solid #3a3738}
.nav a:first-child{padding-left:30px}
.nav a:nth-child(5){border-right:none}
.social{margin-left:auto;margin-right:33px;display:flex;gap:4px}
.social i{display:block;width:20px;height:19px;background:#6a6768}
.social i+i{background:#8e8b8c}

/* hero */
.hero{left:73px;top:140px;width:694px;height:270px;overflow:hidden;
  background:radial-gradient(ellipse at 25% 40%,#e8251c 0%,#f05a18 30%,transparent 60%),radial-gradient(ellipse at 80% 55%,#8cc43a 0%,#b9d22c 35%,transparent 70%),linear-gradient(100deg,#f28a1a,#f7b21c 55%,#a4cb36)}
.hero-copy{position:absolute;left:93px;top:36px;color:var(--ink);font-family:var(--head)}
.hero-copy h1{font-size:24px;font-weight:700;line-height:26px}
.hero-copy p{font-size:22px;line-height:25px;text-transform:uppercase}
.hero-btn{position:absolute;left:93px;top:135px}
.arc{position:absolute;width:250px;height:250px;border-radius:50%;background:var(--white)}

/* buttons */
.btn{display:inline-block;background:var(--ink);color:var(--white);font-size:9.5px;text-transform:uppercase;border-radius:4px;padding:0 13px;height:24px;line-height:24px}

/* features */
.feature{width:232px;text-align:center}
.feature-icon{width:50px;height:54px;margin:0 auto;border-radius:6px}
.feature h2{font-family:var(--head);font-size:17px;font-weight:700;color:var(--ink);margin-top:14px}
.feature p{font-size:9.5px;line-height:13px;color:#333;margin:10px auto 0;width:170px}
.feature .btn{margin-top:14px}

/* sidebar */
.sidebar{left:73px;top:546px;width:146px}
.sidebar-title{height:31px;background:var(--panel);border:1px solid #d4d4d4;border-radius:3px;font-family:var(--head);font-size:12.5px;line-height:29px;padding-left:9px;color:var(--ink)}
.print-list{list-style:none;margin-top:8px;width:129px}
.print-list li{height:25px;border-bottom:1px solid var(--line);font-size:8.5px;text-transform:uppercase;display:flex;align-items:center;gap:9px;color:#222;white-space:nowrap}
.print-list li:last-child{border-bottom:none}
.print-list li::before{content:"";flex:none;width:10px;height:8px;background:var(--ink);border-radius:1px}
.tool-promo{margin-top:12px;width:146px;height:135px;border-radius:3px;padding:16px 0 0 13px;position:relative;
  background:radial-gradient(circle at 80% 20%,#5bc0de,transparent 55%),radial-gradient(circle at 20% 85%,#e8892c,transparent 55%),linear-gradient(135deg,#6a3d8e,#c63c6c 50%,#2f7fb3)}
.tool-promo h3{font-family:var(--head);font-size:16px;line-height:18px;color:var(--ink);font-weight:400}
.tool-promo h3 small{display:block;font-size:12.5px}
.tool-promo p{font-size:9px;line-height:12px;color:#222;margin-top:5px;text-transform:uppercase}
.tool-promo .btn-yellow{position:absolute;left:35px;top:95px;background:var(--yellow);color:#333;font-size:9px;border-radius:4px;height:19px;line-height:19px;padding:0 9px}

/* main column */
.upload{left:230px;top:546px;width:536px;height:107px;background:var(--panel);border:1px solid #d8d8d8;border-radius:3px}
.upload h2{position:absolute;left:19px;top:14px;font-family:var(--head);font-size:16px;font-weight:700;color:var(--green)}
.upload p{position:absolute;left:19px;top:37px;font-size:8.5px;color:#333}
.upload .cta{position:absolute;left:328px;top:10px;font-family:"Kaushan Script",cursive;font-size:24px;color:var(--red);text-transform:uppercase;letter-spacing:.5px}
.file-field{position:absolute;left:16px;top:64px;width:344px;height:31px;border:1px solid #cfcfcf;border-radius:4px;background:var(--white);overflow:hidden}
.file-field span{position:absolute;right:0;top:0;width:69px;height:31px;background:#8f8f8f;color:var(--white);font-size:9.5px;text-align:center;line-height:31px}
.file-types{position:absolute;left:382px;top:67px;display:flex;gap:6px}
.file-types svg{display:block}

.shipping{left:230px;top:658px;width:536px;height:67px;border-radius:3px;
  background:radial-gradient(ellipse at 60% 40%,#f4d52a,transparent 60%),linear-gradient(100deg,#e8821e,#8ab52c 50%,#e7a31f 80%,#8cbf3a)}
.shipping strong{position:absolute;left:40px;top:10px;font-family:var(--head);font-size:40px;color:var(--white);letter-spacing:.5px}
.shipping span{position:absolute;left:344px;top:19px;font-family:var(--head);font-size:16px;color:var(--ink);line-height:16px}
.shipping span small{display:block;font-size:12px;color:#333}

.offers-title{left:231px;top:741px;font-family:var(--head);font-size:16.5px;font-weight:700;color:var(--ink)}
.pager{left:721px;top:739px;display:flex;gap:4px}
.pager i{width:22px;height:18px;background:var(--ink);border-radius:2px;display:flex;align-items:center;justify-content:center}
.product{width:125px}
.product-shot{width:101px;height:100px;border:1px solid #e0e0e0;border-radius:5px;box-shadow:0 1px 3px rgba(0,0,0,.08);display:flex;align-items:center;justify-content:center}
.product-shot div{width:72px;height:60px;border-radius:3px}
.product h3{font-size:7.5px;font-weight:400;color:#222;margin-top:9px}
.product p{font-size:7.5px;line-height:12px;color:var(--muted);margin-top:7px;text-transform:uppercase;white-space:nowrap}
.price{font-size:13px;color:#444;margin-top:6px}
.product .btn{margin-top:8px;height:22px;line-height:22px;font-size:8px;padding:0 10px}

/* footer */
.footer-shadow{left:80px;top:1003px;width:680px;height:6px;border-radius:50%;box-shadow:0 5px 8px rgba(0,0,0,.18)}
.footer-col h4{font-family:var(--body);font-size:11.5px;font-weight:400;color:var(--ink);text-transform:uppercase}
.footer-col ul{list-style:none;margin-top:14px}
.footer-col li{font-size:7.5px;line-height:14px;color:#a5a5a5;text-transform:uppercase}
.footer-contact .addr{font-size:7.5px;color:#999;margin-top:14px}
.footer-contact .tel{font-size:14px;color:#777;margin-top:3px}
.footer-icons{display:flex;gap:4px;margin-top:6px}
.footer-icons i{width:17px;height:17px;background:#b9b9b9;border-radius:2px}
.footer-contact .copy{font-size:7px;color:#555;margin-top:7px}
.pay{display:flex;gap:3px;margin-top:7px}
.pay i{width:28px;height:17px;border-radius:2px;border:1px solid #ccc}
</style>
</head>
<body>
<div class="page-bg"></div>

<div class="abs lang">choose language:
  <svg width="18" height="11" viewBox="0 0 18 11" aria-label="English"><rect width="18" height="11" fill="#22408c"/><path d="M0 0L18 11M18 0L0 11" stroke="#fff" stroke-width="2"/><rect x="7.5" width="3" height="11" fill="#fff"/><rect y="4" width="18" height="3" fill="#fff"/><rect x="8.2" width="1.6" height="11" fill="#c8102e"/><rect y="4.7" width="18" height="1.6" fill="#c8102e"/></svg>
  <svg width="18" height="11" viewBox="0 0 18 11" aria-label="German"><rect width="18" height="3.7" fill="#111"/><rect y="3.7" width="18" height="3.7" fill="#d00"/><rect y="7.3" width="18" height="3.7" fill="#fc0"/></svg>
  <svg width="18" height="11" viewBox="0 0 18 11" aria-label="Spanish"><rect width="18" height="11" fill="#c60b1e"/><rect y="2.75" width="18" height="5.5" fill="#ffc400"/></svg>
</div>

<div class="abs brand"><div class="brand-name">Mosavik Studio</div></div>

<div class="abs contact"><span>Call Us:</span>1 800 555 0142<br><span>Email:</span>hello@mosavikstudio.com</div>

<div class="abs cart">
  <div class="cart-icon"><svg width="14" height="12" viewBox="0 0 14 12"><path d="M0 1h2.5l2 7h7l1.5-5H4" fill="none" stroke="#fff" stroke-width="1.3"/><circle cx="5.5" cy="10.5" r="1.1" fill="#fff"/><circle cx="10.5" cy="10.5" r="1.1" fill="#fff"/></svg></div>
  <div><b>SHOPPING CART</b><small>0 item(s) - $0.00</small></div>
</div>

<nav class="abs nav">
  <a>Home</a><a>Service</a><a>Submission of works</a><a>FAQ's</a><a>About us</a>
  <div class="social"><i></i><i></i></div>
</nav>

<section class="abs hero" role="img" aria-label="Abstract swirls of red, orange and green colour">
  <div class="hero-copy"><h1>WE ADD COLORS</h1><p>Offering the higest quality<br>printing products</p></div>
  <div class="hero-btn"><span class="btn">Know more</span></div>
  <div class="arc" style="left:-11px;top:198px"></div>
  <div class="arc" style="left:222px;top:168px"></div>
  <div class="arc" style="left:455px;top:198px"></div>
</section>

<div class="abs feature" style="left:72px;top:349px">
  <div class="feature-icon" role="img" aria-label="Paint palette with brush" style="background:linear-gradient(135deg,#e2b97a,#b8864a)"></div>
  <h2>JOB SUBMIT</h2>
  <p>Sed ut perspiciatis unde omnis iste natus error sit voluptatem accusantium dolorelaudantium.</p>
  <span class="btn">Get started</span>
</div>
<div class="abs feature" style="left:305px;top:340px">
  <div class="feature-icon" role="img" aria-label="Drawing tools with set square" style="background:linear-gradient(135deg,#9aa4ad,#e2a23a);height:63px;width:62px"></div>
  <h2>JOB DESIGN</h2>
  <p>Sed ut perspiciatis unde omnis iste natus error sit voluptatem accusantium dolorelaudantium.</p>
  <span class="btn">Get started</span>
</div>
<div class="abs feature" style="left:542px;top:349px">
  <div class="feature-icon" role="img" aria-label="Flame" style="background:radial-gradient(circle at 50% 70%,#ffd24a,#f07a16 60%,#e0401a);border-radius:50% 50% 40% 40%"></div>
  <h2>ASK FOR OFFER</h2>
  <p>Sed ut perspiciatis unde omnis iste natus error sit voluptatem accusantium dolorelaudantium.</p>
  <span class="btn">Get started</span>
</div>

<aside class="abs sidebar">
  <div class="sidebar-title">WHAT WE PRINT</div>
  <ul class="print-list">
    <li>Acrylic signs</li><li>Banner designing</li><li>Booklets</li><li>Booklet folders</li><li>Brochures</li>
    <li>Brochures holder</li><li>Bumper stickers</li><li>Business card stickers</li><li>Business postcard</li><li>Calendars</li>
  </ul>
  <div class="tool-promo" role="img" aria-label="Colourful bokeh light background">
    <h3>TRY OUR<small>ONLINE DESIGN TOOL</small></h3>
    <p>Create your files online<br>and ready to print</p>
    <span class="btn-yellow">GET STARTED</span>
  </div>
</aside>

<section class="abs upload">
  <h2>DO YOU HAVE A FILE READY FOR PRINT?</h2>
  <p>ORDER YOUR PRINT ONLINE AND LET US PRINT YOUR FILE FOR YOU</p>
  <div class="cta">Get Started!</div>
  <div class="file-field"><span>BROWSE</span></div>
  <div class="file-types">
    <svg width="24" height="26" viewBox="0 0 24 26"><path d="M1 1h16l6 6v18H1z" fill="#f2f2f2" stroke="#999"/><text x="12" y="19" font-size="6" font-family="Arimo,sans-serif" text-anchor="middle" fill="#777">PDF</text></svg>
    <svg width="24" height="26" viewBox="0 0 24 26"><path d="M1 1h16l6 6v18H1z" fill="#f2f2f2" stroke="#999"/><text x="12" y="19" font-size="6" font-family="Arimo,sans-serif" text-anchor="middle" fill="#777">PSD</text></svg>
    <svg width="24" height="26" viewBox="0 0 24 26"><path d="M1 1h16l6 6v18H1z" fill="#f2f2f2" stroke="#999"/><text x="12" y="19" font-size="6" font-family="Arimo,sans-serif" text-anchor="middle" fill="#777">AI</text></svg>
    <svg width="24" height="26" viewBox="0 0 24 26"><path d="M1 1h16l6 6v18H1z" fill="#f2f2f2" stroke="#999"/><text x="12" y="19" font-size="6" font-family="Arimo,sans-serif" text-anchor="middle" fill="#777">CDR</text></svg>
    <svg width="24" height="26" viewBox="0 0 24 26"><path d="M1 1h16l6 6v18H1z" fill="#f2f2f2" stroke="#999"/><text x="12" y="19" font-size="6" font-family="Arimo,sans-serif" text-anchor="middle" fill="#777">DOC</text></svg>
  </div>
</section>

<section class="abs shipping" role="img" aria-label="Free shipping banner on a bright orange and green abstract background">
  <strong>FREE SHIPPING</strong>
  <span>ON ORDER OVER $100<small>VALID ON ALL OUR PRODUCTS</small></span>
</section>

<h2 class="abs offers-title">LATEST OFFERS</h2>
<div class="abs pager">
  <i><svg width="8" height="9" viewBox="0 0 8 9"><path d="M6 1L2 4.5 6 8" fill="none" stroke="#fff" stroke-width="2"/></svg></i>
  <i><svg width="8" height="9" viewBox="0 0 8 9"><path d="M2 1l4 3.5L2 8" fill="none" stroke="#fff" stroke-width="2"/></svg></i>
</div>

<article class="abs product" style="left:231px;top:775px">
  <div class="product-shot"><div role="img" aria-label="Stack of coloured folders" style="background:linear-gradient(160deg,#7fc7a4,#3a6fb3)"></div></div>
  <h3>FUSCE MASSA IPSUM</h3><p>Donec vitae diam ut purut<br>facilisis. Nullam.</p>
  <div class="price">$2.99</div><span class="btn">Add to cart</span>
</article>
<article class="abs product" style="left:374px;top:775px">
  <div class="product-shot"><div role="img" aria-label="Yellow printed mug" style="background:linear-gradient(#f2c42c,#e0a21a);width:52px;border-radius:4px 4px 10px 10px"></div></div>
  <h3>FUSCE MASSA IPSUM</h3><p>Donec vitae diam ut purut<br>facilisis. Nullam.</p>
  <div class="price">$5.99</div><span class="btn">Add to cart</span>
</article>
<article class="abs product" style="left:518px;top:775px">
  <div class="product-shot"><div role="img" aria-label="Black leather notebooks" style="background:linear-gradient(135deg,#3a3a3a,#111)"></div></div>
  <h3>FUSCE MASSA IPSUM</h3><p>Donec vitae diam ut purut<br>facilisis. Nullam.</p>
  <div class="price">$2.59</div><span class="btn">Add to cart</span>
</article>
<article class="abs product" style="left:661px;top:775px;width:110px">
  <div class="product-shot"><div role="img" aria-label="Disc folder with blue cover" style="background:linear-gradient(90deg,#2a2a2a 40%,#2a5fa8 40%)"></div></div>
  <h3>FUSCE MASSA IPSUM</h3><p>Donec vitae diam ut purut<br>facilisis. Nullam.</p>
  <div class="price">$7.99</div><span class="btn">Add to cart</span>
</article>

<div class="abs footer-shadow"></div>

<div class="abs footer-col" style="left:73px;top:1038px">
  <h4>Information</h4>
  <ul><li>About us</li><li>Customer service</li><li>Privacy policy</li><li>Site map</li><li>Search terms</li><li>Advanced search</li><li>Orders and returns</li><li>Contact us</li></ul>
</div>
<div class="abs footer-col" style="left:227px;top:1038px">
  <h4>Why buy from us</h4>
  <ul><li>Shipping &amp; returns</li><li>Secure shopping</li><li>International shipping</li><li>Affiliates</li><li>Group sales</li></ul>
</div>
<div class="abs footer-col" style="left:381px;top:1038px">
  <h4>My account</h4>
  <ul><li>Sign in</li><li>View cart</li><li>My wishlist</li><li>Track my order</li><li>Help</li></ul>
</div>
<div class="abs footer-col footer-contact" style="left:524px;top:1038px">
  <h4>Contacts</h4>
  <div class="addr">4120 HARBOUR LANE, REYKJAVIK, R10 42KL</div>
  <div class="tel">TEL: +1 (800) 555 01 78</div>
  <div class="footer-icons"><i></i><i></i><i></i></div>
  <div class="copy">© MOSAVIK STUDIO. ALL RIGHTS RESERVED</div>
  <div class="pay"><i style="background:#e9e4d8"></i><i style="background:#e3e7f1"></i><i style="background:#dfeaf3"></i><i style="background:#f3ece2"></i><i style="background:#e2e2e2"></i><i style="background:#eef0f4"></i></div>
</div>
</body>
</html>
```